Iconic website for iconic products

We want a website which will stand out, which will reflect that we are offering cutting edge solutions, breaking the mould. The website must be very search engine friendly, to drive traffic from all around the world, and also sticky, so that they explore what we have to offer, and hopefully buy from us.

We have launched a portfolio of products in the field of 3D, which are highly accessible. They are accessible in their openness, their ease of use and their ultra low cost. We are providing everyone everywhere the opportunity to engage in 3D design and to produce physical 3D models as outputs from their designs. This technology is ground breaking and world changing.

The website will need to be easy for us to maintain and grow, easy for our customers and prospects to use, easy to find.

We will need to integrate a blog, and provide eCommerce capability. We will also be looking to add a forum, which we will need to monitor and maintain, so that our customers can connect with one another, share best practice, offer solutions to problems, and generate value for one another, while reducing our after-sales support burden.

We will also need to set up page templates for our key customers to show what they have done with our products so that others can share the experience.

Target Market(s)

We have a number of distinct markets.
Education:
Primary (5-11) schools
Secondary (11-18) schools
Colleges (16-19)
Universities
Creative designers and designer-makers
Industrial companies; any that are involved in design, in manufacture, in marketing
Animation, games and virtual world organisations
Hobbyists

Industry/Entity Type

Sales

Requirements
Must have
• Iconic design
• Ease of maintenance and future build
• Blog
• eCommerce
• Forum
• Twitter
• When people enquire, people must fill in forms to download information, and we must capture that information on a database.
• We also need a secure log in area for distributors and resellers to access for confidential information.
Nice to have
• An updated logo to match the website
Should not have
• Old fashioned design
• Bricks and mortar feel

```html
<!DOCTYPE html>
<html lang="en">
<head>
<meta charset="utf-8">
<title>Vertex3 Technologies</title>
<link href="https://fonts.googleapis.com/css2?family=Questrial&family=Ubuntu:wght@500;700&family=Noto+Sans:wght@400;700&family=Dancing+Script:wght@700&display=swap" rel="stylesheet">
<style>
:root{
  --red:#b30a0f;
  --red-dark:#8c0006;
  --red-panel:#c9262b;
  --dark:#231f20;
  --charcoal:#2e2a2b;
  --grey:#d6d6d6;
  --text:#222;
  --white:#fff;
}
*{margin:0;padding:0;box-sizing:border-box}
html,body{width:942px;height:1200px;overflow:hidden}
body{background:radial-gradient(ellipse at 50% 40%,#3a3334 0%,#2a2324 60%,#1f1a1b 100%);font-family:"Noto Sans",sans-serif;color:var(--text);position:relative}
.abs{position:absolute}
.header{left:113px;top:6px;width:717px;height:119px}
.header-contact{left:131px;top:30px;color:var(--white);font-family:"Ubuntu",sans-serif}
.header-contact .label{font-size:10px;font-weight:700}
.header-contact .call{position:absolute;left:27px;top:25px;font-size:13px;line-height:17px;white-space:nowrap;font-weight:500}
.header-contact .call b{font-weight:700}
.phone-icon{position:absolute;left:0;top:24px}
.brand{left:300px;top:26px;width:360px;text-align:center;color:var(--white);font-family:"Ubuntu",sans-serif;font-weight:700;font-size:25px;line-height:29px;letter-spacing:.3px}
.follow{left:730px;top:30px;width:82px;text-align:right;color:var(--white);font-family:"Ubuntu",sans-serif;font-size:10px;font-weight:700}
.social{left:744px;top:49px;width:70px;display:grid;grid-template-columns:28px 28px;gap:9px 9px;justify-content:end}
.social span{height:28px;border-radius:5px;background:#f2f2f2;color:var(--red-dark);font-family:"Ubuntu",sans-serif;font-size:8px;font-weight:700;display:flex;align-items:center;justify-content:center}
.nav{left:113px;top:125px;width:717px;height:28px;background:linear-gradient(#3a3536,#1e1a1b)}
.nav a{position:absolute;top:0;height:34px;line-height:18px;padding-top:3px;color:var(--white);text-decoration:none;font-family:"Ubuntu",sans-serif;font-weight:700;font-size:11px;text-align:center;white-space:nowrap}
.nav a.center{width:0;display:flex;justify-content:center}
.nav a.active{background:var(--red)}
.hero{left:113px;top:150px;width:717px;height:233px;background:var(--white)}
.hero-photo{left:2px;top:6px;width:712px;height:227px;background:linear-gradient(100deg,#3a3334 0%,#2a2526 60%,#1f1b1c 100%);border-top-left-radius:4px}
.hero-model{left:10px;top:16px;width:400px;height:190px;background:radial-gradient(ellipse at 55% 45%,#ee3a3a 0%,#d62020 40%,#b58b77 75%,rgba(58,51,52,0) 100%)}
.caption{left:2px;top:209px;width:712px;height:24px;background:rgba(90,85,86,.85);color:var(--white);font-family:"Dancing Script",cursive;font-size:14px;line-height:24px;padding-left:12px}
.caption b{font-family:"Ubuntu",sans-serif;font-size:15px}
.login{left:649px;top:191px;width:191px;height:132px;background:var(--red);box-shadow:2px 3px 4px rgba(0,0,0,.4);padding:16px 9px 0 9px;color:var(--white)}
.login h3{font-family:"Ubuntu",sans-serif;font-weight:500;font-size:13px;padding-left:30px;margin-bottom:6px}
.lock{position:absolute;left:6px;top:12px}
.login .field{height:18px;background:var(--white);border:1px solid #eee;margin-bottom:6px;font-size:8px;color:#aaa;padding:3px 5px}
.login .btn{display:inline-block;background:linear-gradient(#f4f4f4,#c8c8c8);color:#222;font-family:"Ubuntu",sans-serif;font-weight:700;font-size:9px;padding:3px 12px;border-radius:3px;margin-top:2px}
.login .forgot{position:absolute;right:24px;top:89px;font-size:7px}
.content{left:113px;top:383px;width:717px;height:787px;background:var(--white)}
h2{font-family:"Questrial",sans-serif;font-weight:400;color:var(--red-dark)}
.main{left:135px;width:470px;font-size:9px;line-height:13.5px}
.main p{margin-bottom:13.5px}
.more{font-weight:700;font-size:8px;display:flex;align-items:center;gap:4px}
.more i{display:inline-block;width:9px;height:9px;background:var(--red-dark);position:relative}
.more i:after{content:"";position:absolute;left:2px;top:2px;border-left:4px solid #fff;border-top:2.5px solid transparent;border-bottom:2.5px solid transparent}
.bullets{list-style:none}
.bullets li{height:18px;padding-left:12px;position:relative}
.bullets li:before{content:"»";position:absolute;left:0;top:-2px;color:var(--red);font-weight:700;font-size:11px}
.shot{background:linear-gradient(135deg,#3d5a86,#7b6e72 50%,#c79a67);border:1px solid #555}
.card{left:132px;width:381px;height:83px;background:#f6f6f6;padding:6px 4px}
.card h2{font-size:14px}
.card .sub{font-size:9px;line-height:13.5px}
.card .cta{font-size:8px;font-weight:700;margin-top:7px;letter-spacing:.3px}
.panel{left:617px;width:198px;background:linear-gradient(#d93237,#b9161c);border-radius:7px;box-shadow:0 1px 3px rgba(0,0,0,.3);color:var(--white)}
.panel h3{font-family:"Ubuntu",sans-serif;font-weight:500;font-size:17px;position:absolute;white-space:nowrap}
.panel .lbl{position:absolute;left:13px;font-size:9px;font-weight:700}
.panel .inp{position:absolute;left:13px;width:171px;height:19px;background:var(--white);border:1px solid #bbb}
.pbtn{position:absolute;top:267px;width:64px;height:21px;background:linear-gradient(#fafafa,#d5d5d5);color:#222;font-family:"Ubuntu",sans-serif;font-weight:700;font-size:9px;text-align:center;line-height:21px;border:1px solid #999}
.footer{left:0;top:1170px;width:942px;height:30px;background:linear-gradient(#a0060b,#c2141a);color:var(--white);font-size:7px;font-weight:700;line-height:27px}
</style>
</head>
<body>

<!-- header -->
<svg class="abs header" width="717" height="119" viewBox="0 0 717 119">
  <path d="M25 0 H692 Q717 0 717 25 V119 H0 V25 Q0 0 25 0Z" fill="#262122"/>
  <path d="M130 119 C200 68 250 56 300 56 L430 56 C490 56 540 68 640 119Z" fill="#d8d8d8"/>
  <path d="M100 0 C165 55 240 106 366 108 C492 106 568 55 636 0Z" fill="#b30a0f"/>
  <path d="M100 0 C165 55 240 106 366 108 C492 106 568 55 636 0" fill="none" stroke="#7d0005" stroke-width="2"/>
</svg>
<div class="abs header-contact">
  <div class="label">Contact Us!</div>
  <svg class="phone-icon" width="24" height="26" viewBox="0 0 24 26">
    <circle cx="12" cy="14" r="11" fill="#e6e6e6"/>
    <rect x="8" y="6" width="8" height="15" rx="2" fill="#444"/>
    <rect x="9.5" y="8" width="5" height="4" fill="#ddd"/>
  </svg>
  <div class="call">Call Now<br><b>0700 900 4321</b></div>
</div>
<div class="abs brand">Vertex3<br>Technologies</div>
<div class="abs follow">Follow Us on!</div>
<div class="abs social"><span>Posts</span><span>Page</span><span>Chat</span><span>Feed</span></div>

<!-- navigation -->
<nav class="abs nav">
  <a class="active" style="left:63px;width:69px">Home</a>
  <a class="center" style="left:185px">Product</a>
  <a class="center" style="left:275px">Gallery</a>
  <a class="center" style="left:360px">News</a>
  <a class="center" style="left:447px">Contact</a>
  <a class="center" style="left:534px">Order</a>
  <a class="center" style="left:617px">Forum</a>
</nav>

<!-- hero -->
<div class="abs hero">
  <div class="abs hero-photo"></div>
  <div class="abs hero-model" role="img" aria-label="Photo of a hand holding a red 3D printed roof model"></div>
  <div class="abs caption">Incredibly low cost <b>3D</b> technologies for designing and producing 3d models</div>
</div>
<svg class="abs" style="left:113px;top:150px" width="717" height="20" viewBox="0 0 717 20">
  <path d="M1 6 Q358 30 716 0" fill="none" stroke="#fff" stroke-width="2"/>
</svg>

<form class="abs login">
  <svg class="lock" width="22" height="22" viewBox="0 0 22 22">
    <path d="M6 9 V6 a5 5 0 0 1 10 0 V9" fill="none" stroke="#ddd" stroke-width="2.5"/>
    <rect x="3" y="9" width="16" height="11" rx="2" fill="#e0b640"/>
  </svg>
  <h3>Member Login</h3>
  <div class="field">Email id:</div>
  <div class="field">Password:</div>
  <span class="btn">Log In</span>
  <span class="forgot">Forgot Password?</span>
</form>

<!-- content -->
<div class="abs content"></div>

<section class="abs main" style="top:401px">
  <h2 style="font-size:19.5px;margin-bottom:11px">Welcome to Vertex3 Technologies</h2>
  <p>Lorem Ipsum is simply dummy text of the printing and typesetting industry. Lorem Ipsum has been the industry's standard dummy text ever since the 1500s, when an unknown printer took a galley of type and scrambled it to make a type specimen book.</p>
  <p>It has survived not only five centuries, but also the leap into electronic typesetting, remaining essentially unchanged. It was popularised in the 1960s with the release of Typeline sheets containing Lorem Ipsum passages, and more recently with desktop publishing software like Pagewright Studio including versions of Lorem Ipsum.</p>
  <div class="more"><i></i>Read More</div>
</section>

<section class="abs main" style="top:591px">
  <h2 style="font-size:19px">Our Products Range</h2>
  <div>below are our full range of products..</div>
</section>

<section class="abs main" style="top:648px">
  <h2 style="font-size:18.5px">MORPHIX 3D creative solution</h2>
  <div class="abs" style="left:329px;top:8px;font-size:9.5px;font-weight:700">PRICE: £ 495.00</div>
  <div style="width:240px;margin-top:10px">
    <p>The easy way to design creative 3D models on a PC without having to learn or use 3D CAD.</p>
    <p>Morphix is a cutting edge ‘haptic’ technology which delivers a high quality, immersive 3D ....</p>
  </div>
</section>
<div class="abs shot" style="left:392px;top:681px;width:147px;height:108px" role="img" aria-label="Photo of a laptop with a haptic 3D pen device"></div>

<section class="abs main" style="top:774px">
  <div style="font-weight:700;margin-bottom:4px">Morphix’s WOW factors:</div>
  <ul class="bullets">
    <li>Use our 3D mouse to 'touch' and feel the 3 dimensional qualities of a virtual object</li>
    <li>Movement in all directions to manipulate and construct objects within a 3D space</li>
    <li>Sense of touching and moving freely, tapping into your natural way of doing things</li>
    <li>Feel where you are, whether inside or outside objects</li>
    <li>So easy to create organic shapes</li>
    <li>Change the hardness/softness of virtual objects for different effects</li>
    <li>Straightforward interface for a more intuitive way to sketch and model</li>
  </ul>
  <div class="more" style="margin-top:6px"><i></i>Other Products</div>
</section>

<article class="abs card" style="top:948px">
  <h2>Morphix 3D creative</h2>
  <div class="sub"><b>package from £350</b><br>for designing creative 3D models</div>
  <div class="cta">Click for more information</div>
</article>
<div class="abs shot" style="left:393px;top:951px;width:97px;height:77px;background:radial-gradient(ellipse,#cfe3e6 0%,#6c8fb8 45%,#1f2f7a 100%)" role="img" aria-label="Photo of a printed organic lattice model"></div>

<article class="abs card" style="top:1046px">
  <h2>Orbit 3D Laserscanner</h2>
  <div class="sub"><b>from £320</b><br>for creating virtual 3D models from real objects</div>
  <div class="cta">Click for more information</div>
</article>
<div class="abs shot" style="left:393px;top:1049px;width:97px;height:77px;background:linear-gradient(#f4f0ea,#c99a66 50%,#f4f0ea)" role="img" aria-label="Photo of three scanned figurine models"></div>

<div class="abs main" style="top:1143px"><div class="more"><i></i>Other Products</div></div>

<!-- sidebar: video -->
<aside class="abs panel" style="top:406px;height:189px">
  <svg class="abs" style="left:7px;top:5px" width="30" height="24" viewBox="0 0 30 24">
    <rect x="1" y="6" width="26" height="16" rx="3" fill="#222"/>
    <circle cx="14" cy="14" r="6" fill="#555" stroke="#999"/>
    <rect x="5" y="2" width="8" height="5" fill="#222"/>
  </svg>
  <h3 style="left:46px;top:10px">Video Section</h3>
  <div class="abs" style="left:18px;top:37px;width:162px;height:108px;background:radial-gradient(ellipse at 50% 55%,#5a5fd0 0%,#5a3a30 45%,#2a1a14 100%)" role="img" aria-label="Video still of a desktop 3D printer at work"></div>
  <svg class="abs" style="left:18px;top:145px" width="162" height="20" viewBox="0 0 162 20">
    <rect width="162" height="20" fill="#fff"/>
    <path d="M7 5 L15 10 L7 15Z" fill="#333"/>
    <rect x="64" y="8" width="50" height="4" rx="2" fill="#ccc"/>
    <circle cx="68" cy="10" r="3" fill="#333"/>
    <rect x="120" y="6" width="10" height="7" fill="none" stroke="#333"/>
    <path d="M136 8 h3 l3-3 v10 l-3-3 h-3z" fill="#333"/>
  </svg>
  <svg class="abs" style="left:92px;top:81px" width="16" height="16" viewBox="0 0 16 16"><path d="M3 1 L15 8 L3 15Z" fill="#fff"/></svg>
  <div class="abs" style="left:0;width:198px;top:171px;text-align:center;font-size:8px;font-weight:700;letter-spacing:.3px">More Videos</div>
</aside>

<!-- sidebar: enquiry -->
<form class="abs panel" style="top:613px;height:300px">
  <svg class="abs" style="left:5px;top:6px" width="36" height="34" viewBox="0 0 36 34">
    <path d="M3 12 L20 4 L30 20 L13 30Z" fill="#fff"/>
    <path d="M22 18 L34 2" stroke="#d8b25c" stroke-width="3"/>
  </svg>
  <h3 style="left:52px;top:15px">Enquiry Now</h3>
  <span class="lbl" style="top:43px">Name</span>
  <span class="inp" style="top:55px"></span>
  <span class="lbl" style="top:88px">E-mail</span>
  <span class="inp" style="top:100px"></span>
  <span class="lbl" style="top:130px">Subject</span>
  <span class="inp" style="top:145px"></span>
  <span class="lbl" style="top:172px">Comments</span>
  <span class="inp" style="top:182px;height:76px"></span>
  <span class="pbtn" style="left:34px">Submit</span>
  <span class="pbtn" style="left:103px">Clear</span>
</form>

<!-- sidebar: blog -->
<aside class="abs panel" style="top:934px;height:189px">
  <svg class="abs" style="left:10px;top:4px" width="38" height="38" viewBox="0 0 38 38">
    <rect x="1" y="1" width="36" height="36" rx="8" fill="#f08a24" stroke="#fff" stroke-width="2"/>
    <circle cx="11" cy="27" r="3.5" fill="#fff"/>
    <path d="M8 17 a13 13 0 0 1 13 13 M8 9 a21 21 0 0 1 21 21" fill="none" stroke="#fff" stroke-width="4"/>
  </svg>
  <h3 style="left:56px;top:12px">Recent Blog Post</h3>
  <div class="abs" style="left:11px;top:58px;width:85px;height:58px;background:linear-gradient(90deg,#3a4f7a,#7c8db0 60%,#d9d9d9)" role="img" aria-label="Blog thumbnail about fair pricing"></div>
  <div class="abs" style="left:106px;top:87px;font-size:9px;font-weight:700;line-height:10.5px">Topic By<br>R.T. Vance<br><span style="font-weight:400">01-05-2010</span></div>
  <div class="abs" style="left:11px;top:129px;width:180px;font-size:8.5px;font-weight:700;line-height:10.5px">Lorem Ipsum is simply dummy text of the printing and typesetting industry.</div>
  <div class="abs" style="right:17px;top:171px;font-size:8px;font-weight:700">Read More</div>
</aside>

<!-- footer -->
<footer class="abs footer">
  <span class="abs" style="left:136px">Copyright© Vertex3 Technologies Ltd 2009-2010 &nbsp;| &nbsp;All Rights Reserved.</span>
  <span class="abs" style="right:127px">Contact Us | Privacy | Sitemap</span>
</footer>

</body>
</html>
```